Meadowbrook Holdings Website Design

We have been redeveloping our website already and are quite happy with the content, but the design needs to be better:
https://trelvan-site.examplehost.net/

Pages, content, concept etc. Can all be taken from the redeveloped website.
The farmer can register and edit/view their profile, subscribe and these pages need to be designed better as well as contact, about, pricing, tos, privacy and a page with example portlets.

We need a website to appeal to farmers, investors and retiring farmers.

The design should be clean and a little country.

We don't want any repeat designs that some may submit to every project and has no respect for the project brief, so please don't submit them.

Target Market(s)

farmers, investors, retirees

Industry/Entity Type

Farming

Number of Pages Required

5+ page

Colors

Designer to choose colors to be used in the design.

Requirements
Must have
• Nice, clean modern design that is appealing
• Profile page laid out nicely

```html
<!DOCTYPE html>
<html lang="en">
<head>
<meta charset="utf-8">
<title>Meadowbrook Holdings</title>
<link href="https://fonts.googleapis.com/css2?family=Lato:wght@400;700;900&display=swap" rel="stylesheet">
<style>
:root{
  --green:#22a637;
  --green-dark:#1b8a2d;
  --ink:#3a3a3a;
  --grey:#6b6b6b;
  --icon-grey:#777;
  --white:#fff;
}
*{margin:0;padding:0;box-sizing:border-box}
html,body{width:954px;height:1200px;overflow:hidden;background:var(--white);font-family:'Lato',sans-serif;color:var(--ink)}
.page{position:relative;width:954px;height:1200px}
.abs{position:absolute}
.btn{position:absolute;background:var(--green);color:var(--white);font-size:13px;display:flex;align-items:center;justify-content:center;text-transform:uppercase;letter-spacing:.2px}

.topbar{left:0;top:0;width:954px;height:22px;background:var(--green);color:var(--white);font-size:9px;font-weight:700}
.topbar .phone{left:137px;top:6px;font-weight:400}
.topbar .account{left:511px;top:6px;letter-spacing:.1px}
.topbar .account span{font-weight:400;margin:0 5px}
.topbar .social{left:762px;top:5px;display:flex;gap:8px}
.topbar .social i{display:block;width:11px;height:11px;border-radius:50%;background:var(--white)}

.navbar{left:0;top:22px;width:954px;height:53px;border-bottom:1px solid #e4e4e4}
.brand{left:137px;top:18px;display:flex;align-items:center;gap:6px;font-size:14px;font-weight:900;color:var(--green);text-transform:uppercase}
.brand i{display:block;width:14px;height:14px;border-radius:50%;background:var(--green)}
.menu{left:358px;top:20px;display:flex;gap:21px;font-size:11px;text-transform:uppercase;color:#444}
.menu .active{color:var(--green);font-weight:700}

.hero{left:0;top:75px;width:954px;height:323px;background:linear-gradient(180deg,#5b6670 0%,#3f5a3a 35%,#55663c 70%,#4b5a30 100%)}
.hero h1{position:absolute;left:0;width:954px;top:86px;text-align:center;color:var(--white);font-size:20px;font-weight:900;line-height:22px;letter-spacing:-.3px}
.hero .rule{position:absolute;top:153px;height:2px;background:var(--green);width:193px}
.hero .dot{position:absolute;left:470px;top:147px;width:14px;height:14px;border:1.5px solid var(--white);border-radius:50%}
.hero p{position:absolute;left:0;width:954px;top:174px;text-align:center;color:var(--white);font-size:12px}

.profile{left:0;top:398px;width:954px;height:179px}
.profile .text{left:137px;top:43px;width:310px}
.profile h2{font-size:15px;font-weight:900;text-transform:uppercase;color:#333;letter-spacing:-.2px;margin-bottom:6px}
.profile p{font-size:10px;line-height:13px;color:var(--grey)}
.profile .media{left:470px;top:0;width:484px;height:179px;background:radial-gradient(ellipse at 70% 20%,#3fa54a 0%,var(--green-dark) 60%,#1f8a2e 100%)}
.video{position:absolute;top:41px;width:157px;height:96px;border:2px solid var(--white);background:linear-gradient(180deg,#8a6a55,#5a4033)}
.video.workshop{background:linear-gradient(180deg,#4a5a7a,#5a3f3a)}
.video .bar{position:absolute;left:0;bottom:0;width:100%;height:6px;background:#111}

.ownership{left:0;top:577px;width:954px;height:268px;background:linear-gradient(180deg,#2f3523 0%,#434426 50%,#3a361f 100%)}
.ownership h2{position:absolute;left:0;width:954px;top:77px;text-align:center;font-size:29px;font-weight:900;color:var(--white);letter-spacing:-.5px}
.ownership p{position:absolute;left:277px;width:400px;top:116px;text-align:center;font-size:10px;line-height:13px;color:var(--white)}
.pager{position:absolute;top:209px;height:3px;width:24px;background:var(--white)}
.pager.on{background:var(--green)}

.own h2{position:absolute;left:0;width:954px;top:902px;text-align:center;font-size:30px;font-weight:900;color:var(--green);letter-spacing:-.5px}
.own p{position:absolute;left:0;width:954px;top:944px;text-align:center;font-size:10.5px;line-height:13px;color:var(--grey)}
.own p a{color:var(--green)}
.step{position:absolute;top:1005px;width:160px;text-align:center}
.step .ring{margin:0 auto;width:107px;height:107px;border-radius:50%;background:var(--white);box-shadow:0 1px 4px rgba(0,0,0,.35);display:flex;align-items:center;justify-content:center}
.step .ring.fill{background:var(--green);border:4px solid var(--white)}
.step h3{margin-top:10px;font-size:11px;font-weight:900;line-height:11px;color:var(--icon-grey);text-transform:uppercase}
</style>
</head>
<body>
<div class="page">
  <header class="abs topbar">
    <div class="abs phone">PHONE NUMBER:- 0800 4172905</div>
    <div class="abs account">MY ACCOUNT<span>|</span>LOGIN<span>|</span>CREAT AN ACCOUNT</div>
    <div class="abs social"><i></i><i></i><i></i></div>
  </header>

  <nav class="abs navbar">
    <div class="abs brand"><i></i>Meadowbrook Holdings</div>
    <div class="abs menu">
      <span class="active">Home</span><span>Aspiring Farmers</span><span>Investors</span><span>Retiring Farmer</span><span>Pricing</span><span>Blog</span>
    </div>
  </nav>

  <section class="abs hero" role="img" aria-label="Farming family walking through a pasture with a rider on horseback and grazing cattle">
    <h1>WE PROVIDE ADVICE WHEN YOUR BUSINESS NEEDS IT.<br>NOT JUST WHEN YOU ASK FOR IT!</h1>
    <div class="rule" style="left:256px"></div>
    <div class="dot"></div>
    <div class="rule" style="left:507px"></div>
    <p>Lorem ipsum dolor sit amet, consetetur sadipscing of elitr, sed diam nonumy .</p>
    <div class="btn" style="left:428px;top:208px;width:99px;height:26px">Login In</div>
  </section>

  <section class="abs profile">
    <div class="abs text">
      <h2>Callum Rigby &amp; Ewan Tate</h2>
      <p>I really love to farm as farming is forever. I would love to farm any-where there is an opportunity to live and work in a local farming community.</p>
    </div>
    <div class="btn" style="left:137px;top:117px;width:118px;height:26px">View Profile</div>
    <div class="abs media">
      <div class="video" style="left:16px" role="img" aria-label="Video of a young farmer talking to camera indoors"><div class="bar"></div></div>
      <div class="video workshop" style="left:189px" role="img" aria-label="Video of a farmer speaking in front of a tractor"><div class="bar"></div></div>
    </div>
  </section>

  <section class="abs ownership" role="img" aria-label="Herd of cattle moving across a paddock at dusk with a rider on horseback">
    <h2>FARM OWNERSHIP</h2>
    <p>I really love to farm as farming is forever. I would love to farm anywhere there is an opportunity to live and work in a local farming community.</p>
    <div class="btn" style="left:417px;top:161px;width:118px;height:26px">Sign Up Now</div>
    <div class="pager on" style="left:420px"></div>
    <div class="pager" style="left:449px"></div>
    <div class="pager" style="left:478px"></div>
    <div class="pager" style="left:508px"></div>
  </section>

  <section class="own">
    <h2>YOU CAN OWN A FARM</h2>
    <p>We know how hard it is for a young family to find the capital required to own and operate their own farm - so we started <a>Meadowbrook Holdings</a>.<br>We want to rejuvenate regional Australia by putting farming back up the top of the career list for anyone.</p>

    <div class="step" style="left:136px">
      <div class="ring">
        <svg width="56" height="56" viewBox="0 0 56 56" fill="none" stroke="#777" stroke-width="2.5">
          <circle cx="17" cy="14" r="8"/><circle cx="39" cy="14" r="8"/><circle cx="28" cy="32" r="6"/>
          <path d="M5 40c0-10 5-15 12-15M51 40c0-10-5-15-12-15M18 52c0-7 4-11 10-11s10 4 10 11z"/>
        </svg>
      </div>
      <h3>We connect a young<br>farming family</h3>
    </div>

    <div class="step" style="left:310px">
      <div class="ring fill">
        <svg width="60" height="60" viewBox="0 0 60 60" fill="#fff">
          <circle cx="22" cy="16" r="10"/><circle cx="38" cy="24" r="10"/>
          <path d="M4 44c0-12 8-18 18-18 5 0 8 1 10 3-6 3-8 9-8 15z"/>
          <path d="M20 56c0-12 8-18 18-18s18 6 18 18z"/>
        </svg>
      </div>
      <h3>With a retiring<br>farming family</h3>
    </div>

    <div class="step" style="left:483px">
      <div class="ring">
        <svg width="56" height="56" viewBox="0 0 56 56" fill="#777">
          <circle cx="22" cy="14" r="9"/><circle cx="34" cy="14" r="9"/>
          <path d="M6 46c0-13 7-20 16-20h12c9 0 16 7 16 20z"/>
          <circle cx="38" cy="40" r="10" fill="#fff" stroke="#777" stroke-width="2.5"/>
          <path d="M38 33v14M41 36h-4a2 2 0 0 0 0 4h2a2 2 0 0 1 0 4h-4" fill="none" stroke="#777" stroke-width="2"/>
        </svg>
      </div>
      <h3>And investors</h3>
    </div>

    <div class="step" style="left:658px">
      <div class="ring">
        <svg width="60" height="56" viewBox="0 0 60 56" fill="#777" role="img" aria-label="Barn and ploughed field">
          <path d="M40 6l12 8v16H28V14z"/>
          <rect x="4" y="14" width="24" height="3"/>
          <path d="M2 50l20-22h6L10 50zM14 50l18-20h6L22 50zM26 50l18-20h8L36 50zM40 50l14-18v18z"/>
        </svg>
      </div>
      <h3>To own and operate<br>a farm together</h3>
    </div>
  </section>
</div>
</body>
</html>
```